Infectious Diseases Research Laboratory Needs Business Card

We need a business card for an academic research laboratory based in Kansas City called VELKOR. The full lab name is Microbe Exposure Kinetics/Response Modeling Integrated Study Laboratory, but this does not need to be incorporated. We study novel ways to optimize the treatment of multidrug-resistant bacterial infections ("superbugs") throughout the entire biomedical research spectrum (from benchtop to bedside). The name VELKOR is not only an acronym for our lab name, but also represents our desire to make discoveries and explore the unknown (the stars, if you well). It also serves as an ode to the state of Kansas motto where we are based, ad astra per aspera ("to the stars, through difficulty").

Target Market(s)

Pharmaceutical companies, researchers

Industry/Entity Type

Pharmaceutical

Contact Information for Business Card

The business card should incorporate and complement our new logo (see uploaded files). Double-sided designs are preferred. Looking for something modern, but professional.

Font styles to use
Sans Serif

Requirements
Must have
• Double-sided. One side would ideally be a solid color incorporating logo and the other should also have the logo (smaller), but incorporate staff information.
• Color codes:
• Red: #F04C51
• Blue: #3477B5
• Gray: #808285

```html
<!DOCTYPE html>
<html lang="en">
<head>
<meta charset="utf-8">
<title>VELKOR Business Card</title>
<link rel="stylesheet" href="https://fonts.googleapis.com/css2?family=Montserrat:wght@300;400&family=Open+Sans:wght@400;600&display=swap">
<style>
  :root {
    --red: #F04C51;
    --blue: #3477B5;
    --gray: #808285;
    --ink: #4a4b4d;
    --cream: #F3F0E6;
    --backdrop: #D9D9D9;
    --white: #FFFFFF;
  }
  * { margin: 0; padding: 0; box-sizing: border-box; }
  html, body {
    width: 1200px; height: 786px; overflow: hidden;
    background: var(--backdrop);
  }
  .sheet {
    width: 1200px; height: 786px;
    display: flex; align-items: center; justify-content: center; gap: 40px;
  }
  .card {
    position: relative;
    width: 520px; height: 297px;
    border-radius: 16px;
    overflow: hidden;
    box-shadow: 0 6px 18px rgba(0,0,0,0.18);
  }

  /* Front: staff details */
  .card--front { background: var(--cream); }
  .card__swoosh { position: absolute; inset: 0; }
  .brand {
    position: absolute; left: 34px; top: 38px;
    display: flex; align-items: center; gap: 12px;
  }
  .brand__dot {
    width: 34px; height: 34px; border-radius: 50%;
    background: var(--red);
  }
  .brand__name {
    font-family: "Montserrat", sans-serif;
    font-weight: 300;
    font-size: 40px;
    letter-spacing: 5px;
    color: var(--red);
  }
  .staff {
    position: absolute; left: 300px; top: 120px;
    font-family: "Open Sans", sans-serif;
    color: var(--ink);
  }
  .staff__name {
    font-family: "Montserrat", sans-serif;
    font-weight: 400;
    font-size: 17px;
    letter-spacing: 0.5px;
    color: var(--red);
    text-transform: uppercase;
  }
  .staff__role { font-size: 12px; color: var(--gray); margin-bottom: 12px; }
  .contact { list-style: none; font-size: 12px; line-height: 18px; }
  .contact__item { display: flex; align-items: center; gap: 8px; }
  .contact__icon { width: 11px; height: 11px; flex: none; }
  .address { font-size: 12px; line-height: 17px; margin-top: 6px; }

  /* Back: solid colour with name */
  .card--back {
    background: var(--red);
    display: flex; align-items: center; justify-content: center; gap: 16px;
  }
  .card--back .brand__dot { width: 46px; height: 46px; background: var(--white); }
  .card--back .brand__name { color: var(--white); font-size: 52px; letter-spacing: 7px; }
</style>
</head>
<body>
<main class="sheet">
  <section class="card card--front" aria-label="Business card front">
    <svg class="card__swoosh" viewBox="0 0 520 297" aria-hidden="true">
      <path d="M0,178 C90,232 190,268 262,297 L0,297 Z" fill="var(--blue)"/>
      <path d="M0,152 C95,214 200,262 290,297" fill="none" stroke="var(--red)" stroke-width="5"/>
      <path d="M0,166 C92,224 196,266 276,297" fill="none" stroke="var(--white)" stroke-width="3"/>
    </svg>

    <div class="brand">
      <span class="brand__dot"></span>
      <span class="brand__name">VELKOR</span>
    </div>

    <div class="staff">
      <p class="staff__name">Maren Holcott</p>
      <p class="staff__role">Director</p>
      <ul class="contact">
        <li class="contact__item">
          <svg class="contact__icon" viewBox="0 0 12 12" aria-hidden="true"><path d="M3 1 L5 3.5 L4 5 C4.8 6.6 5.6 7.4 7 8 L8.5 7 L11 9 L9.8 11 C5 10.5 1.5 7 1 2.2 Z" fill="var(--red)"/></svg>
          <span>816-555-0142</span>
        </li>
        <li class="contact__item">
          <svg class="contact__icon" viewBox="0 0 12 12" aria-hidden="true"><rect x="0.5" y="2.5" width="11" height="7" fill="var(--red)"/><path d="M0.5 2.5 L6 7 L11.5 2.5" fill="none" stroke="var(--white)" stroke-width="1"/></svg>
          <span>info@velkor.org</span>
        </li>
        <li class="contact__item">
          <svg class="contact__icon" viewBox="0 0 12 12" aria-hidden="true"><circle cx="6" cy="6" r="5.2" fill="var(--red)"/><path d="M1 6 H11 M6 1 C3.5 4 3.5 8 6 11 M6 1 C8.5 4 8.5 8 6 11" fill="none" stroke="var(--white)" stroke-width="0.8"/></svg>
          <span>www.velkor.org</span>
        </li>
      </ul>
      <p class="address">4470 Rockhill Road<br>Kansas City, MO 64110</p>
    </div>
  </section>

  <section class="card card--back" aria-label="Business card back">
    <span class="brand__dot"></span>
    <span class="brand__name">VELKOR</span>
  </section>
</main>
</body>
</html>
```